Web App Dashboard Design for Healthcare Company

We have developed a simple web application with 3 navigation menus. We like the current design (very much modeled after Tallyworks), but we want to explore UI options for the branding, header, menus, and footer that we may not have considered.

The attached screenshots show the layout and two menu "hover" views as they currently exist.

This web application is used by employees only.

Menu 1 - Module Menu:
Allows the user to switch easily between Account, Employee, and Care Management.

Menu 2 - Reports Menu
Allows user to view available reports within each Module.

Menu 3 - Admin Menu
Allows the user to easily create new content types within each module.

Use our branded colors and font.

Colors:
Logo Blue (dark): 00c0f3
Logo Blue (light): 44c8f5
Nav Blue: 0994d0
Green: 71b44b
Grayscale: (not specified)

Font:
Lato (Google Font)

Target Market(s)

Internal staff.

Industry/Entity Type

Healthcare

Number of Pages Required

3 page

Font styles to use
Sans Serif
Other font styles liked:
• Lato (Google Font)

Colors
0293ce
9bcb3c

Requirements
Must have
• It's really a one page design, but we want to see the two "hover" views for the Module Menu and the Admin Menu.
• It should also be very clear which "Report" page the user is on (the active menu link).
• Must use branded colors, font, and logo.
• Logo Blue (dark): 00c0f3
• Logo Blue (light): 44c8f5
• Nav Blue: 0994d0
• Green: 71b44b
• Grayscale: Designer may choose
Nice to have
• It would be nice to have simple uncluttered payouts.
Should not have
• The design should not have menu options exposed by default.

```html
<!DOCTYPE html>
<html lang="en">
<head>
<meta charset="utf-8">
<title>Medvela – Web App Design</title>
<link rel="stylesheet" href="https://fonts.googleapis.com/css2?family=Lato:wght@400;700&family=Saira+Condensed:wght@300&display=swap">
<style>
  :root{
    --page:#6f82ab;
    --backdrop:#dcdfe4;
    --dark:#17191c;
    --dark-2:#202327;
    --dark-3:#28313a;
    --white:#ffffff;
    --zebra:#f0f1f2;
    --text:#2b2b2b;
    --muted:#8a8d91;
    --nav-blue:#0994d0;
    --logo-blue:#00c0f3;
    --green:#71b44b;
    --title-green:#8cc63f;
    --red:#e53935;
    --line:#e3e4e6;
  }
  *{box-sizing:border-box;margin:0;padding:0}
  html,body{width:670px;height:1200px;overflow:hidden}
  body{background:var(--page);font-family:"Lato",sans-serif;color:var(--text);position:relative}

  .screen{position:absolute;left:10px;width:651px;height:368px;overflow:hidden;background:var(--backdrop)}
  .screen--list{top:10px}
  .screen--admin{top:387px}
  .screen--modules{top:765px}
  .backdrop{position:absolute;inset:58px 0 0 0;background:linear-gradient(180deg,#e2e5e9,#d3d7dc)}

  .topbar{position:absolute;left:0;top:0;width:100%;height:58px;background:var(--dark)}
  .brand{position:absolute;left:22px;top:24px;display:flex;align-items:center;gap:5px;color:var(--white);font-weight:700;font-size:12px}
  .brand-mark{width:9px;height:9px;background:var(--logo-blue)}
  .module-title{position:absolute;left:0;width:100%;top:9px;text-align:center;color:var(--title-green);font-size:13.5px;letter-spacing:.2px}
  .module-title svg{vertical-align:middle;margin-left:3px}
  .user-links{position:absolute;right:24px;top:7px;display:flex;align-items:center;gap:14px;font-size:6.5px;color:var(--white);letter-spacing:.2px}
  .logout{border:1px solid #8d9096;border-radius:10px;padding:4px 7px}

  .panel{position:absolute;left:86px;top:30px;width:479px;height:338px;background:var(--white);border-radius:3px 3px 0 0}
  .tabs{height:26px;display:flex;position:relative;font-size:6.6px;color:#3a3a3a}
  .tab{position:absolute;top:9px}
  .tab--active{color:var(--green)}
  .tab--active::after{content:"";position:absolute;left:-3px;right:-3px;top:12px;height:1.5px;background:var(--green)}

  .table-head,.row{position:relative;height:24px;font-size:7.6px}
  .table-head{position:absolute;top:27px;left:0;right:0;height:23px;background:var(--nav-blue);color:var(--white)}
  .rows{position:absolute;top:50px;left:0;right:0}
  .row:nth-child(even){background:var(--zebra)}
  .cell{position:absolute;top:50%;transform:translateY(-50%);white-space:nowrap}
  .c1{left:9px}.c2{left:97px}.c3{left:153px}.c4{left:194px}.c5{left:283px}.c6{left:348px}.c7{left:411px}
  .status{width:11px;height:11px;display:block}
  .row .c3{transform:translateY(-50%)}
  .table-head .c3{left:153px}

  .pager{position:absolute;top:300px;left:0;right:0;display:flex;justify-content:center;align-items:center;gap:9px;font-size:8px;color:#555}
  .pager .current{color:var(--nav-blue)}
  .pager-btn{width:14px;height:14px;border-radius:50%;background:var(--nav-blue);display:flex;align-items:center;justify-content:center}
  .pager .p-prev{margin-right:10px}.pager .p-next{margin-left:10px}

  .legal{position:absolute;top:328px;left:0;right:0;text-align:center;font-size:5.3px;color:#8a8a8a}
  .legal a{color:var(--nav-blue);text-decoration:none}

  .fab{position:absolute;left:589px;top:315px;width:38px;height:38px;border-radius:50%;display:flex;align-items:center;justify-content:center;box-shadow:0 2px 5px rgba(0,0,0,.3)}
  .fab--add{background:var(--green)}
  .fab--close{background:var(--red)}

  .admin-menu{position:absolute;left:479px;top:205px;width:134px;height:133px;background:var(--dark);border-radius:4px;padding-top:5px;box-shadow:0 3px 10px rgba(0,0,0,.35)}
  .admin-item{height:29px;display:flex;align-items:center;padding-left:14px;gap:11px;color:#e4e6e8;font-size:7.6px}
  .admin-item--active{background:var(--dark-3);color:var(--nav-blue)}

  .module-switcher{position:absolute;left:0;top:0;width:100%;height:126px;background:var(--dark)}
  .module-card{position:absolute;top:24px;width:115px;height:56px;border:1px solid #5c6066;border-radius:3px;background:var(--dark-2);color:#a7abb0;font-size:7.4px;text-align:center}
  .module-card svg{display:block;margin:7px auto 4px}
  .module-card--active{border-color:var(--green);color:var(--green)}
  .module-card--accounts{left:134px}.module-card--employees{left:268px}.module-card--care{left:402px}
  .cancel{position:absolute;left:508px;top:112px;width:95px;height:28px;border-radius:14px;background:#d32f2f;color:var(--white);font-size:7.6px;font-weight:700;display:flex;align-items:center;justify-content:center;box-shadow:0 2px 5px rgba(0,0,0,.35)}

  .showcase-foot{position:absolute;left:0;top:1140px;width:100%;height:60px}
  .foot-brand{position:absolute;left:24px;top:20px;display:flex;align-items:center;gap:6px;font-weight:700;font-size:16px;color:var(--dark)}
  .foot-brand .brand-mark{width:12px;height:12px}
  .foot-title{position:absolute;left:0;width:100%;top:10px;text-align:center;font-family:"Saira Condensed",sans-serif;font-weight:300;font-size:26px;color:#eef0f5;letter-spacing:.5px}
</style>
</head>
<body>
<svg width="0" height="0" style="position:absolute">
  <defs>
    <symbol id="ok" viewBox="0 0 12 12"><circle cx="6" cy="6" r="6" fill="#4caf50"/><path d="M3.3 6.2l1.8 1.8 3.6-3.7" fill="none" stroke="#fff" stroke-width="1.4" stroke-linecap="round" stroke-linejoin="round"/></symbol>
    <symbol id="no" viewBox="0 0 12 12"><circle cx="6" cy="6" r="6" fill="#e53935"/><path d="M4 4l4 4M8 4l-4 4" stroke="#fff" stroke-width="1.4" stroke-linecap="round"/></symbol>
    <symbol id="chev-down" viewBox="0 0 10 6"><path d="M1 1l4 4 4-4" fill="none" stroke="#8cc63f" stroke-width="1.6"/></symbol>
    <symbol id="prev" viewBox="0 0 8 8"><path d="M5 1.5L2.5 4 5 6.5" fill="none" stroke="#fff" stroke-width="1.4"/></symbol>
    <symbol id="next" viewBox="0 0 8 8"><path d="M3 1.5L5.5 4 3 6.5" fill="none" stroke="#fff" stroke-width="1.4"/></symbol>
    <symbol id="plus" viewBox="0 0 16 16"><path d="M8 2v12M2 8h12" stroke="#fff" stroke-width="2" stroke-linecap="round"/></symbol>
    <symbol id="cross" viewBox="0 0 16 16"><path d="M3.5 3.5l9 9M12.5 3.5l-9 9" stroke="#fff" stroke-width="2" stroke-linecap="round"/></symbol>
  </defs>
</svg>

<!-- Screen: default list view -->
<section class="screen screen--list">
  <div class="backdrop" role="img" aria-label="Light grey backdrop with faint healthcare line icons"></div>
  <header class="topbar">
    <div class="brand"><span class="brand-mark"></span>Medvela</div>
    <div class="module-title">ACCOUNTS MANAGEMENT<svg width="9" height="6"><use href="#chev-down"/></svg></div>
    <nav class="user-links"><span>MY INFO</span><span class="logout">LOG OUT</span></nav>
  </header>
  <main class="panel">
    <nav class="tabs">
      <span class="tab tab--active" style="left:20px">REMINDERS</span>
      <span class="tab" style="left:82px">ACCOUNTS</span>
      <span class="tab" style="left:141px">PATIENT REQUESTS</span>
      <span class="tab" style="left:226px">REPORTS</span>
      <span class="tab" style="left:277px">MY COMPANY</span>
    </nav>
    <div class="table-head"><span class="cell c1">Sample Text</span><span class="cell c2">Label Two</span><span class="cell c3">Tab</span><span class="cell c4">Random Message</span><span class="cell c5">Caption</span><span class="cell c6">Testing</span><span class="cell c7">Last Column</span></div>
    <div class="rows">
      <div class="row"><span class="cell c1">Lorem ipsum</span><span class="cell c2">One</span><svg class="cell c3 status"><use href="#ok"/></svg><span class="cell c4">Etiam risus lorem</span><span class="cell c5">1Caption</span><span class="cell c7">Completed</span></div>
      <div class="row"><span class="cell c1">Integer vulputate</span><span class="cell c2">Two</span><svg class="cell c3 status"><use href="#ok"/></svg><span class="cell c4">Praesent id justo</span><span class="cell c5">2Caption</span><span class="cell c6">Testing</span><span class="cell c7">Completed</span></div>
      <div class="row"><span class="cell c1">Lorem ipsum</span><span class="cell c2">Three</span><svg class="cell c3 status"><use href="#no"/></svg><span class="cell c4">Etiam risus lorem</span><span class="cell c5">3Caption</span><span class="cell c7">Missed</span></div>
      <div class="row"><span class="cell c1">Integer vulputate</span><span class="cell c2">Four</span><svg class="cell c3 status"><use href="#ok"/></svg><span class="cell c4">Praesent id justo</span><span class="cell c5">4Caption</span><span class="cell c6">Testing</span><span class="cell c7">Completed</span></div>
      <div class="row"><span class="cell c1">Integer vulputate</span><span class="cell c2">Five</span><svg class="cell c3 status"><use href="#no"/></svg><span class="cell c5">5Caption</span><span class="cell c6">Testing</span><span class="cell c7">Missed</span></div>
      <div class="row"><span class="cell c1">Integer vulputate</span><span class="cell c2">Six</span><svg class="cell c3 status"><use href="#no"/></svg><span class="cell c4">Etiam risus lorem</span><span class="cell c5">6Caption</span><span class="cell c7">Missed</span></div>
      <div class="row"><span class="cell c1">Lorem ipsum</span><span class="cell c2">Seven</span><svg class="cell c3 status"><use href="#ok"/></svg><span class="cell c4">Praesent id justo</span><span class="cell c5">7Caption</span><span class="cell c6">Testing</span><span class="cell c7">Completed</span></div>
      <div class="row"><span class="cell c1">Integer vulputate</span><span class="cell c2">Eight</span><svg class="cell c3 status"><use href="#ok"/></svg><span class="cell c4">Etiam risus lorem</span><span class="cell c5">8Caption</span><span class="cell c7">Completed</span></div>
      <div class="row"><span class="cell c1">Lorem ipsum</span><span class="cell c2">Nine</span><svg class="cell c3 status"><use href="#ok"/></svg><span class="cell c5">9Caption</span><span class="cell c6">Testing</span><span class="cell c7">Completed</span></div>
      <div class="row"><span class="cell c1">Integer vulputate</span><span class="cell c2">Ten</span><svg class="cell c3 status"><use href="#no"/></svg><span class="cell c4">Praesent id justo</span><span class="cell c5">10Caption</span><span class="cell c6">Testing</span><span class="cell c7">Missed</span></div>
    </div>
    <nav class="pager"><span class="pager-btn p-prev"><svg width="8" height="8"><use href="#prev"/></svg></span><span>1</span><span class="current">2</span><span>3</span><span>4</span><span>5</span><span class="pager-btn p-next"><svg width="8" height="8"><use href="#next"/></svg></span></nav>
    <footer class="legal">Medvela ™ | Copyright © 2016. All Rights Reserved. <a>Get Started</a> | <a>About Us</a> | <a>Contact Us</a> | <a>Terms &amp; Agreement</a> | <a>Privacy Policy</a></footer>
  </main>
  <div class="fab fab--add"><svg width="15" height="15"><use href="#plus"/></svg></div>
</section>

<!-- Screen: admin menu open -->
<section class="screen screen--admin">
  <div class="backdrop" role="img" aria-label="Light grey backdrop with faint healthcare line icons"></div>
  <header class="topbar">
    <div class="brand"><span class="brand-mark"></span>Medvela</div>
    <div class="module-title">ACCOUNTS MANAGEMENT<svg width="9" height="6"><use href="#chev-down"/></svg></div>
    <nav class="user-links"><span>MY INFO</span><span class="logout">LOG OUT</span></nav>
  </header>
  <main class="panel">
    <nav class="tabs">
      <span class="tab tab--active" style="left:20px">REMINDERS</span>
      <span class="tab" style="left:82px">ACCOUNTS</span>
      <span class="tab" style="left:141px">PATIENT REQUESTS</span>
      <span class="tab" style="left:226px">REPORTS</span>
      <span class="tab" style="left:277px">MY COMPANY</span>
    </nav>
    <div class="table-head"><span class="cell c1">Sample Text</span><span class="cell c2">Label Two</span><span class="cell c3">Tab</span><span class="cell c4">Random Message</span><span class="cell c5">Caption</span><span class="cell c6">Testing</span><span class="cell c7">Last Column</span></div>
    <div class="rows">
      <div class="row"><span class="cell c1">Lorem ipsum</span><span class="cell c2">One</span><svg class="cell c3 status"><use href="#ok"/></svg><span class="cell c4">Etiam risus lorem</span><span class="cell c5">1Caption</span><span class="cell c7">Completed</span></div>
      <div class="row"><span class="cell c1">Integer vulputate</span><span class="cell c2">Two</span><svg class="cell c3 status"><use href="#ok"/></svg><span class="cell c4">Praesent id justo</span><span class="cell c5">2Caption</span><span class="cell c6">Testing</span><span class="cell c7">Completed</span></div>
      <div class="row"><span class="cell c1">Lorem ipsum</span><span class="cell c2">Three</span><svg class="cell c3 status"><use href="#no"/></svg><span class="cell c4">Etiam risus lorem</span><span class="cell c5">3Caption</span><span class="cell c7">Missed</span></div>
      <div class="row"><span class="cell c1">Integer vulputate</span><span class="cell c2">Four</span><svg class="cell c3 status"><use href="#ok"/></svg><span class="cell c4">Praesent id justo</span><span class="cell c5">4Caption</span><span class="cell c6">Testing</span><span class="cell c7">Completed</span></div>
      <div class="row"><span class="cell c1">Integer vulputate</span><span class="cell c2">Five</span><svg class="cell c3 status"><use href="#no"/></svg><span class="cell c5">5Caption</span><span class="cell c6">Testing</span><span class="cell c7">Missed</span></div>
      <div class="row"><span class="cell c1">Integer vulputate</span><span class="cell c2">Six</span><svg class="cell c3 status"><use href="#no"/></svg><span class="cell c4">Etiam risus lorem</span><span class="cell c5">6Caption</span></div>
      <div class="row"><span class="cell c1">Lorem ipsum</span><span class="cell c2">Seven</span><svg class="cell c3 status"><use href="#ok"/></svg><span class="cell c4">Praesent id justo</span><span class="cell c5">7Caption</span><span class="cell c6">Testing</span></div>
      <div class="row"><span class="cell c1">Integer vulputate</span><span class="cell c2">Eight</span><svg class="cell c3 status"><use href="#ok"/></svg><span class="cell c4">Etiam risus lorem</span><span class="cell c5">8Caption</span></div>
      <div class="row"><span class="cell c1">Lorem ipsum</span><span class="cell c2">Nine</span><svg class="cell c3 status"><use href="#ok"/></svg><span class="cell c5">9Caption</span><span class="cell c6">Testing</span></div>
      <div class="row"><span class="cell c1">Integer vulputate</span><span class="cell c2">Ten</span><svg class="cell c3 status"><use href="#no"/></svg><span class="cell c4">Praesent id justo</span><span class="cell c5">10Caption</span><span class="cell c6">Testing</span></div>
    </div>
    <nav class="pager"><span class="pager-btn p-prev"><svg width="8" height="8"><use href="#prev"/></svg></span><span>1</span><span class="current">2</span><span>3</span><span>4</span><span>5</span><span class="pager-btn p-next"><svg width="8" height="8"><use href="#next"/></svg></span></nav>
    <footer class="legal">Medvela ™ | Copyright © 2016. All Rights Reserved. <a>Get Started</a> | <a>About Us</a> | <a>Contact Us</a> | <a>Terms &amp; Agreement</a> | <a>Privacy Policy</a></footer>
  </main>
  <div class="admin-menu">
    <div class="admin-item"><svg width="13" height="11" viewBox="0 0 13 11"><rect x=".5" y=".5" width="12" height="10" rx="1" fill="none" stroke="#c5c8cc"/><circle cx="6.5" cy="4.3" r="1.8" fill="#c5c8cc"/><path d="M3.3 9c.5-1.8 1.7-2.6 3.2-2.6S9.2 7.2 9.7 9z" fill="#c5c8cc"/></svg>Account</div>
    <div class="admin-item"><svg width="13" height="12" viewBox="0 0 13 12"><rect x="1" y=".5" width="6" height="11" fill="none" stroke="#c5c8cc"/><rect x="7" y="4" width="5" height="7.5" fill="none" stroke="#c5c8cc"/><path d="M2.5 2.5h3M2.5 4.5h3M2.5 6.5h3M2.5 8.5h3M8.5 6h2M8.5 8h2" stroke="#c5c8cc"/></svg>Company Contact</div>
    <div class="admin-item admin-item--active"><svg width="13" height="12" viewBox="0 0 13 12"><rect x=".5" y="1.5" width="10" height="10" fill="none" stroke="#0994d0"/><path d="M2.5 4.5h4M2.5 6.5h6M2.5 8.5h5" stroke="#0994d0"/><path d="M8 7l4-6" stroke="#0994d0" stroke-width="1.3"/></svg>Note</div>
    <div class="admin-item"><svg width="13" height="12" viewBox="0 0 13 12"><path d="M1 1h11v7H5l-3 3V8H1z" fill="none" stroke="#c5c8cc"/><path d="M3 3.5h7M3 5.5h5" stroke="#c5c8cc"/></svg>Message</div>
  </div>
  <div class="fab fab--close"><svg width="14" height="14"><use href="#cross"/></svg></div>
</section>

<!-- Screen: module switcher open -->
<section class="screen screen--modules">
  <div class="backdrop" role="img" aria-label="Light grey backdrop with faint healthcare line icons"></div>
  <main class="panel">
    <nav class="tabs">
      <span class="tab tab--active" style="left:20px">REMINDERS</span>
      <span class="tab" style="left:82px">ACCOUNTS</span>
      <span class="tab" style="left:141px">PATIENT REQUESTS</span>
      <span class="tab" style="left:226px">REPORTS</span>
      <span class="tab" style="left:277px">MY COMPANY</span>
    </nav>
    <div class="table-head"><span class="cell c1">Sample Text</span><span class="cell c2">Label Two</span><span class="cell c3">Tab</span><span class="cell c4">Random Message</span><span class="cell c5">Caption</span><span class="cell c6">Testing</span><span class="cell c7">Last Column</span></div>
    <div class="rows">
      <div class="row"><span class="cell c1">Lorem ipsum</span><span class="cell c2">One</span><svg class="cell c3 status"><use href="#ok"/></svg><span class="cell c4">Etiam risus lorem</span><span class="cell c5">1Caption</span><span class="cell c7">Completed</span></div>
      <div class="row"><span class="cell c1">Integer vulputate</span><span class="cell c2">Two</span><svg class="cell c3 status"><use href="#ok"/></svg><span class="cell c4">Praesent id justo</span><span class="cell c5">2Caption</span><span class="cell c6">Testing</span><span class="cell c7">Completed</span></div>
      <div class="row"><span class="cell c1">Lorem ipsum</span><span class="cell c2">Three</span><svg class="cell c3 status"><use href="#no"/></svg><span class="cell c4">Etiam risus lorem</span><span class="cell c5">3Caption</span><span class="cell c7">Missed</span></div>
      <div class="row"><span class="cell c1">Integer vulputate</span><span class="cell c2">Four</span><svg class="cell c3 status"><use href="#ok"/></svg><span class="cell c4">Praesent id justo</span><span class="cell c5">4Caption</span><span class="cell c6">Testing</span><span class="cell c7">Completed</span></div>
      <div class="row"><span class="cell c1">Integer vulputate</span><span class="cell c2">Five</span><svg class="cell c3 status"><use href="#no"/></svg><span class="cell c5">5Caption</span><span class="cell c6">Testing</span><span class="cell c7">Missed</span></div>
      <div class="row"><span class="cell c1">Integer vulputate</span><span class="cell c2">Six</span><svg class="cell c3 status"><use href="#no"/></svg><span class="cell c4">Etiam risus lorem</span><span class="cell c5">6Caption</span><span class="cell c7">Missed</span></div>
      <div class="row"><span class="cell c1">Lorem ipsum</span><span class="cell c2">Seven</span><svg class="cell c3 status"><use href="#ok"/></svg><span class="cell c4">Praesent id justo</span><span class="cell c5">7Caption</span><span class="cell c6">Testing</span><span class="cell c7">Completed</span></div>
      <div class="row"><span class="cell c1">Integer vulputate</span><span class="cell c2">Eight</span><svg class="cell c3 status"><use href="#ok"/></svg><span class="cell c4">Etiam risus lorem</span><span class="cell c5">8Caption</span><span class="cell c7">Completed</span></div>
      <div class="row"><span class="cell c1">Lorem ipsum</span><span class="cell c2">Nine</span><svg class="cell c3 status"><use href="#ok"/></svg><span class="cell c5">9Caption</span><span class="cell c6">Testing</span><span class="cell c7">Completed</span></div>
      <div class="row"><span class="cell c1">Integer vulputate</span><span class="cell c2">Ten</span><svg class="cell c3 status"><use href="#no"/></svg><span class="cell c4">Praesent id justo</span><span class="cell c5">10Caption</span><span class="cell c6">Testing</span><span class="cell c7">Missed</span></div>
    </div>
    <nav class="pager"><span class="pager-btn p-prev"><svg width="8" height="8"><use href="#prev"/></svg></span><span>1</span><span class="current">2</span><span>3</span><span>4</span><span>5</span><span class="pager-btn p-next"><svg width="8" height="8"><use href="#next"/></svg></span></nav>
    <footer class="legal">Medvela ™ | Copyright © 2016. All Rights Reserved. <a>Get Started</a> | <a>About Us</a> | <a>Contact Us</a> | <a>Terms &amp; Agreement</a> | <a>Privacy Policy</a></footer>
  </main>
  <div class="fab fab--add"><svg width="15" height="15"><use href="#plus"/></svg></div>
  <nav class="module-switcher">
    <div class="module-card module-card--accounts module-card--active">
      <svg width="26" height="26" viewBox="0 0 26 26"><circle cx="13" cy="8" r="5" fill="none" stroke="#71b44b" stroke-width="1.4"/><path d="M4 23c0-5 4-9 9-9s9 4 9 9z" fill="none" stroke="#71b44b" stroke-width="1.4"/><path d="M10 19l2.3 2.3 4-4" fill="none" stroke="#71b44b" stroke-width="1.4"/></svg>
      Accounts Management
    </div>
    <div class="module-card module-card--employees">
      <svg width="26" height="26" viewBox="0 0 26 26"><circle cx="15" cy="8" r="4.5" fill="none" stroke="#a7abb0" stroke-width="1.4"/><path d="M7 23c0-4.5 3.6-8 8-8s8 3.5 8 8z" fill="none" stroke="#a7abb0" stroke-width="1.4"/><circle cx="9" cy="9" r="3.5" fill="none" stroke="#a7abb0" stroke-width="1.2"/><path d="M2 21c0-3.5 2.5-6 6-6" fill="none" stroke="#a7abb0" stroke-width="1.2"/></svg>
      Employee Management
    </div>
    <div class="module-card module-card--care">
      <svg width="26" height="26" viewBox="0 0 26 26"><path d="M13 13l-4.5-4.3a2.7 2.7 0 0 1 4.5-3 2.7 2.7 0 0 1 4.5 3z" fill="none" stroke="#a7abb0" stroke-width="1.3"/><path d="M3 17h5l4 2h6l5-3v2l-6 4H9l-6-2z" fill="none" stroke="#a7abb0" stroke-width="1.3" stroke-linejoin="round"/></svg>
      Care Management
    </div>
    <div class="cancel">CANCEL</div>
  </nav>
</section>

<footer class="showcase-foot">
  <div class="foot-brand"><span class="brand-mark"></span>Medvela</div>
  <div class="foot-title">Web App Design</div>
</footer>
</body>
</html>
```